Investment firm needs refreshed corporate powerpoint slides design

We need a new and refreshed powerpoint template for our corporate investment deck. We are a technology private equity group that primarily invests in fast growing software companies and we would like to reflect that in a modern and light blue / transparant / white powerpoint and fonts template. I have also attached our old investor deck as a guideline and also check out our website to get an idea of what we do and what type of companies we invested in. Please note that our website is old and so our presentation should be a refreshed "2017" modern design, not a copy / paste of our website design and graphics.
Updates

Target Market(s)

Investors such as high net worth individuals, pension funds, banks, financial advisors

Industry/Entity Type

Investment

Colors
33a6d7
85cae6
cfeae6
edf8f6
ffffff
fff3d1
86cfc6

Requirements
Must have
• We let you be creative, we trust you have seen more investment presentations before.
Nice to have
• Pre-built models, flow charts, graphs, charts, etc.
Should not have
• Fancy or edgy images, this has to be a modern, fresh and trustworthy looking powerpoint template. No stock images, if you do use stock images for background purposes please be creative! :-)

```html
<!DOCTYPE html>
<html lang="en">
<head>
<meta charset="utf-8">
<title>Harlow — Corporate Deck Template, Part 3</title>
<link href="https://fonts.googleapis.com/css2?family=Lato:wght@400;700;900&family=Montserrat:wght@700;800&display=swap" rel="stylesheet">
<style>
  :root{
    --bg:#0f3b35;
    --panel:#c4c7cc;
    --sky:#33a6d7;
    --sky-soft:#85cae6;
    --mint:#cfeae6;
    --mint-pale:#edf8f6;
    --cream:#fff3d1;
    --teal:#86cfc6;
    --navy:#1c2f6b;
    --ink:#2b3440;
    --grey:#a6a6a6;
    --red:#c00000;
    --dark:#14213d;
    --deepteal:#1d5f6b;
    --muted:#8fa6a3;
  }
  *{box-sizing:border-box;margin:0;padding:0}
  html,body{width:1200px;height:1200px;overflow:hidden}
  body{background:var(--bg);font-family:"Lato",sans-serif;position:relative}
  .sheet-title{position:absolute;top:22px;left:0;width:1200px;text-align:center;
    color:var(--muted);font-size:17px;font-weight:700;letter-spacing:1.5px}
  .board{position:absolute;left:16px;top:333px;width:1157px;height:505px;background:var(--panel);
    display:grid;grid-template-columns:repeat(5,194px);grid-auto-rows:168px;column-gap:43px;padding:6px 10px}
  .frame{position:relative;width:194px;height:168px}
  .slide{display:block;width:194px;height:146px;background:#fff;box-shadow:0 0 0 1px #b5b8bd}
  .page-no{position:absolute;right:0;top:149px;font-size:7px;font-weight:700;color:var(--ink)}
  .slide text{font-family:"Lato",sans-serif}
  .t-title{font-size:6px;font-weight:700;fill:var(--navy)}
  .t-logo{font-size:6.6px;font-weight:400;fill:var(--navy)}
  .t-logo-lg{font-size:11px;font-weight:400;fill:var(--navy)}
  .rule{stroke:var(--sky);stroke-width:.8;stroke-dasharray:5 1.2}
  .foot-rule{stroke:var(--sky);stroke-width:.7;stroke-dasharray:6 1.2}
  .t-foot{font-size:2.6px;fill:#7f93a6}
  .t-brand{font-size:2.8px;font-weight:700;fill:var(--navy)}
  .t-stage{font-size:2.3px;fill:var(--ink);text-anchor:middle}
  .t-chev{font-size:2.2px;fill:#fff;font-weight:700;text-anchor:middle}
  .t-row{font-size:3.2px;fill:#fff;font-weight:700;text-anchor:middle}
  .t-cell{font-size:2.4px;fill:var(--ink)}
  .t-cell-w{font-size:2.4px;fill:#fff}
  .t-bul{font-size:3.1px;fill:var(--ink)}
  .t-agenda{font-size:3.6px;fill:#8fa3b3}
  .t-agenda-on{font-size:4.6px;fill:var(--navy);font-weight:700}
  .t-tiny{font-size:2.1px;fill:var(--ink)}
  .prose{font-family:"Lato",sans-serif;color:#4a5560;text-align:justify}
  .prose p{margin-bottom:1.6px}
  .t-contact-h{font-family:"Montserrat",sans-serif;font-size:7.6px;font-weight:800;fill:var(--dark)}
</style>
</head>
<body>
<div class="sheet-title">PPT DESIGN IDEA- PART 3</div>

<main class="board">

  <!-- 60 Execution model, light -->
  <figure class="frame">
    <svg class="slide" viewBox="0 0 194 146">
      <text x="5" y="12" class="t-title">HL Growth's Execution Model</text>
      <text x="189" y="12" text-anchor="end" class="t-logo">Harlow</text>
      <line x1="5" y1="18" x2="189" y2="18" class="rule"/>
      <g fill="var(--sky)">
        <polygon points="52,27 90,27 94,31.5 90,36 52,36 55,31.5"/>
        <polygon points="96,27 132,27 136,31.5 132,36 96,36 99,31.5"/>
        <polygon points="138,27 180,27 184,31.5 180,36 138,36 141,31.5"/>
      </g>
      <text x="73" y="32.6" class="t-chev">Investment</text>
      <text x="116" y="32.6" class="t-chev">Execution</text>
      <text x="161" y="32.6" class="t-chev">Exit</text>
      <text x="73" y="42" class="t-stage">Stage 1</text><text x="116" y="42" class="t-stage">Stage 2</text><text x="161" y="42" class="t-stage">Stage 3</text>
      <g fill="var(--sky-soft)"><rect x="6" y="47" width="41" height="21"/><rect x="6" y="73" width="41" height="21"/><rect x="6" y="101" width="41" height="21"/></g>
      <g fill="#f4f4f4" stroke="#d8d8d8" stroke-width=".3" stroke-dasharray="1 .6"><rect x="52" y="47" width="40" height="21"/><rect x="52" y="73" width="40" height="21"/><rect x="52" y="101" width="40" height="21"/></g>
      <g fill="var(--cream)"><rect x="94" y="47" width="40" height="21"/><rect x="94" y="73" width="40" height="21"/><rect x="94" y="101" width="40" height="21"/></g>
      <g fill="var(--sky)"><rect x="138" y="47" width="46" height="21"/><rect x="138" y="73" width="46" height="21"/><rect x="138" y="101" width="46" height="21"/></g>
      <text x="26.5" y="59" class="t-row">Company</text><text x="26.5" y="85" class="t-row">HL Growth</text><text x="26.5" y="113" class="t-row">Executive</text>
      <text class="t-cell"><tspan x="55" y="54">$5M-$50M revenue</tspan><tspan x="55" y="58">Founder owned</tspan></text>
      <text class="t-cell"><tspan x="97" y="54">Performance gaps</tspan><tspan x="97" y="58">Efficient tech stack</tspan></text>
      <text class="t-cell-w"><tspan x="141" y="54">Double revenue</tspan><tspan x="141" y="58">Exit in 3-5 years</tspan></text>
      <text class="t-cell"><tspan x="55" y="80">Largest team</tspan><tspan x="55" y="84">Sector specialists</tspan></text>
      <text class="t-cell"><tspan x="97" y="80">Sales and marketing</tspan><tspan x="97" y="84">Pricing and retention</tspan></text>
      <text class="t-cell-w"><tspan x="141" y="80">Retain best talent</tspan><tspan x="141" y="84">Execute growth plan</tspan></text>
      <text class="t-cell"><tspan x="55" y="108">Top 10% operators</tspan><tspan x="55" y="112">Equity partners</tspan></text>
      <text class="t-cell"><tspan x="97" y="107">Peer network</tspan><tspan x="97" y="111">Playbook access</tspan><tspan x="97" y="115">Board support</tspan></text>
      <text class="t-cell-w"><tspan x="141" y="108">Founder equity</tspan><tspan x="141" y="112">Aligned exit</tspan></text>
      <line x1="10" y1="131" x2="184" y2="131" class="foot-rule"/>
      <text x="10" y="138" class="t-foot">Confidential 60</text>
      <text x="184" y="138" text-anchor="end" class="t-brand">HL Growth Equity</text>
    </svg>
    <figcaption class="page-no">60</figcaption>
  </figure>

  <!-- 61 Execution model, bold -->
  <figure class="frame">
    <svg class="slide" viewBox="0 0 194 146">
      <text x="5" y="12" class="t-title">HL Growth's Execution Model</text>
      <text x="189" y="12" text-anchor="end" class="t-logo">Harlow</text>
      <line x1="5" y1="18" x2="189" y2="18" class="rule"/>
      <polygon fill="#c3c3c3" points="52,27 90,27 94,31.5 90,36 52,36 55,31.5"/>
      <polygon fill="#b3b3b3" points="96,27 132,27 136,31.5 132,36 96,36 99,31.5"/>
      <polygon fill="var(--dark)" points="138,27 180,27 184,31.5 180,36 138,36 141,31.5"/>
      <text x="73" y="32.6" class="t-chev">Investment</text><text x="116" y="32.6" class="t-chev">Execution</text><text x="161" y="32.6" class="t-chev">Exit</text>
      <text x="73" y="42" class="t-stage">Stage 1</text><text x="116" y="42" class="t-stage">Stage 2</text><text x="161" y="42" class="t-stage">Stage 3</text>
      <g fill="#1e3a8a"><rect x="6" y="47" width="41" height="21"/><rect x="6" y="73" width="41" height="21"/><rect x="6" y="101" width="41" height="21"/></g>
      <g fill="var(--grey)"><rect x="52" y="47" width="40" height="21"/><rect x="52" y="73" width="40" height="21"/><rect x="52" y="101" width="40" height="21"/><rect x="94" y="47" width="40" height="21"/><rect x="94" y="73" width="40" height="21"/><rect x="94" y="101" width="40" height="21"/></g>
      <g fill="var(--red)"><rect x="138" y="47" width="46" height="21"/><rect x="138" y="73" width="46" height="21"/><rect x="138" y="101" width="46" height="21"/></g>
      <text x="26.5" y="59" class="t-row">Company</text><text x="26.5" y="85" class="t-row">HL Growth</text><text x="26.5" y="113" class="t-row">Executive</text>
      <text class="t-cell-w"><tspan x="55" y="54">$5M-$50M revenue</tspan><tspan x="55" y="58">Founder owned</tspan></text>
      <text class="t-cell-w"><tspan x="97" y="54">Performance gaps</tspan><tspan x="97" y="58">Efficient tech stack</tspan></text>
      <text class="t-cell-w"><tspan x="141" y="54">Double revenue</tspan><tspan x="141" y="58">Exit in 3-5 years</tspan></text>
      <text class="t-cell-w"><tspan x="55" y="80">Largest team</tspan><tspan x="55" y="84">Sector specialists</tspan></text>
      <text class="t-cell-w"><tspan x="97" y="80">Sales and marketing</tspan><tspan x="97" y="84">Pricing and retention</tspan></text>
      <text class="t-cell-w"><tspan x="141" y="80">Retain best talent</tspan><tspan x="141" y="84">Execute growth plan</tspan></text>
      <text class="t-cell-w"><tspan x="55" y="108">Top 10% operators</tspan><tspan x="55" y="112">Equity partners</tspan></text>
      <text class="t-cell-w"><tspan x="97" y="107">Peer network</tspan><tspan x="97" y="111">Playbook access</tspan><tspan x="97" y="115">Board support</tspan></text>
      <text class="t-cell-w"><tspan x="141" y="108">Founder equity</tspan><tspan x="141" y="112">Aligned exit</tspan></text>
      <line x1="10" y1="131" x2="184" y2="131" class="foot-rule"/>
      <text x="10" y="138" class="t-foot">Confidential 61</text>
      <text x="184" y="138" text-anchor="end" class="t-brand">HL Growth Equity</text>
    </svg>
    <figcaption class="page-no">61</figcaption>
  </figure>

  <!-- 62 Execution model, teal steps -->
  <figure class="frame">
    <svg class="slide" viewBox="0 0 194 146">
      <text x="5" y="12" class="t-title">HL Growth's Execution Model</text>
      <text x="189" y="12" text-anchor="end" class="t-logo">Harlow</text>
      <line x1="5" y1="18" x2="189" y2="18" class="rule"/>
      <g fill="var(--deepteal)">
        <rect x="52" y="27" width="38" height="9" rx="4.5"/>
        <rect x="96" y="27" width="36" height="9" rx="4.5"/>
        <rect x="138" y="27" width="42" height="9" rx="4.5"/>
      </g>
      <circle cx="90" cy="31.5" r="4" fill="#f2b705"/><circle cx="132" cy="31.5" r="4" fill="#f2b705"/><circle cx="180" cy="31.5" r="4" fill="#e02020"/>
      <text x="70" y="32.6" class="t-chev">Investment</text><text x="113" y="32.6" class="t-chev">Execution</text><text x="158" y="32.6" class="t-chev">Exit</text>
      <text x="73" y="42" class="t-stage">Stage 1</text><text x="116" y="42" class="t-stage">Stage 2</text><text x="161" y="42" class="t-stage">Stage 3</text>
      <g fill="#1e3a8a"><rect x="6" y="47" width="41" height="21"/><rect x="6" y="73" width="41" height="21"/><rect x="6" y="101" width="41" height="21"/></g>
      <g fill="var(--grey)"><rect x="52" y="47" width="40" height="21"/><rect x="52" y="73" width="40" height="21"/><rect x="52" y="101" width="40" height="21"/><rect x="94" y="47" width="40" height="21"/><rect x="94" y="73" width="40" height="21"/><rect x="94" y="101" width="40" height="21"/></g>
      <g fill="var(--red)"><rect x="138" y="47" width="46" height="21"/><rect x="138" y="73" width="46" height="21"/><rect x="138" y="101" width="46" height="21"/></g>
      <text x="26.5" y="59" class="t-row">Company</text><text x="26.5" y="85" class="t-row">HL Growth</text><text x="26.5" y="113" class="t-row">Executive</text>
      <text class="t-cell-w"><tspan x="55" y="54">$5M-$50M revenue</tspan><tspan x="55" y="58">Founder owned</tspan></text>
      <text class="t-cell-w"><tspan x="97" y="54">Performance gaps</tspan><tspan x="97" y="58">Efficient tech stack</tspan></text>
      <text class="t-cell-w"><tspan x="141" y="54">Double revenue</tspan><tspan x="141" y="58">Exit in 3-5 years</tspan></text>
      <text class="t-cell-w"><tspan x="55" y="80">Largest team</tspan><tspan x="55" y="84">Sector specialists</tspan></text>
      <text class="t-cell-w"><tspan x="97" y="80">Sales and marketing</tspan><tspan x="97" y="84">Pricing and retention</tspan></text>
      <text class="t-cell-w"><tspan x="141" y="80">Retain best talent</tspan><tspan x="141" y="84">Execute growth plan</tspan></text>
      <text class="t-cell-w"><tspan x="55" y="108">Top 10% operators</tspan><tspan x="55" y="112">Equity partners</tspan></text>
      <text class="t-cell-w"><tspan x="97" y="107">Peer network</tspan><tspan x="97" y="111">Playbook access</tspan><tspan x="97" y="115">Board support</tspan></text>
      <text class="t-cell-w"><tspan x="141" y="108">Founder equity</tspan><tspan x="141" y="112">Aligned exit</tspan></text>
      <line x1="10" y1="131" x2="184" y2="131" class="foot-rule"/>
      <text x="10" y="138" class="t-foot">Confidential 62</text>
      <text x="184" y="138" text-anchor="end" class="t-brand">HL Growth Equity</text>
    </svg>
    <figcaption class="page-no">62</figcaption>
  </figure>

  <!-- 63 Equity protection chart -->
  <figure class="frame">
    <svg class="slide" viewBox="0 0 194 146">
      <text x="5" y="12" class="t-title">Equity Protection with Upside Option</text>
      <text x="189" y="12" text-anchor="end" class="t-logo">Harlow</text>
      <line x1="5" y1="18" x2="189" y2="18" class="rule"/>
      <rect x="20" y="25" width="154" height="96" fill="#f4f6f8" stroke="#c9d0d6" stroke-width=".4"/>
      <g stroke="#dde3e8" stroke-width=".3">
        <line x1="20" y1="39" x2="174" y2="39"/><line x1="20" y1="53" x2="174" y2="53"/><line x1="20" y1="67" x2="174" y2="67"/><line x1="20" y1="81" x2="174" y2="81"/><line x1="20" y1="95" x2="174" y2="95"/><line x1="20" y1="109" x2="174" y2="109"/>
        <line x1="72" y1="25" x2="72" y2="121"/><line x1="123" y1="25" x2="123" y2="121"/>
      </g>
      <g stroke="#333" stroke-width=".5"><line x1="20" y1="25" x2="20" y2="121"/><line x1="20" y1="121" x2="174" y2="121"/></g>
      <g class="t-tiny" font-size="1.8"><text x="15" y="40">4x</text><text x="15" y="54">3x</text><text x="15" y="68">2x</text><text x="15" y="82">1x</text><text x="15" y="96">0x</text></g>
      <text transform="translate(9 88) rotate(-90)" class="t-tiny">Investment Multiple</text>
      <line x1="60" y1="98" x2="97" y2="56" stroke="var(--sky)" stroke-width=".5"/>
      <text transform="translate(62 86) rotate(-38)" class="t-tiny" fill="var(--sky)">Target Returns 3-5x</text>
      <text x="44" y="101" class="t-tiny" text-anchor="middle" font-weight="700">PROTECTION</text>
      <rect x="29" y="103" width="31" height="15" fill="var(--sky)"/>
      <text class="t-tiny" fill="#fff"><tspan x="31" y="107">• Preferred return</tspan><tspan x="31" y="110.5">• Senior position</tspan><tspan x="31" y="114">• Asset coverage</tspan></text>
      <text x="97" y="63" class="t-tiny" text-anchor="middle" font-weight="700">OPERATIONAL</text>
      <rect x="82" y="65" width="31" height="37" fill="var(--sky)"/>
      <text class="t-tiny" fill="#fff"><tspan x="84" y="70">• Revenue growth</tspan><tspan x="84" y="75">• Margin gains</tspan><tspan x="84" y="80">• Pricing model</tspan><tspan x="84" y="85">• Churn reduction</tspan><tspan x="84" y="90">• Team upgrades</tspan></text>
      <text x="151" y="29" class="t-tiny" text-anchor="middle" font-weight="700">STRATEGIC</text>
      <rect x="133" y="31" width="36" height="35" fill="var(--sky)"/>
      <text class="t-tiny" fill="#fff"><tspan x="135" y="36">• Add-on buys</tspan><tspan x="135" y="41">• New markets</tspan><tspan x="135" y="46">• Product lines</tspan><tspan x="135" y="51">• Platform scale</tspan><tspan x="135" y="56">• Strategic exit</tspan></text>
      <g stroke="#555" stroke-width=".4" fill="none"><polyline points="60,110 72,110 72,102"/><polyline points="113,80 128,80 128,66"/></g>
      <g class="t-tiny" font-size="1.8" text-anchor="middle"><text x="44" y="125">Downside Risk</text><text x="97" y="125">Base Case Returns</text><text x="148" y="125">Game Changing Upside</text></g>
      <line x1="10" y1="131" x2="184" y2="131" class="foot-rule"/>
      <text x="10" y="138" class="t-foot">Confidential 63</text>
      <text x="70" y="138" class="t-tiny" font-size="1.7">Illustrative only; past results do not guarantee future returns</text>
      <text x="184" y="138" text-anchor="end" class="t-brand">HL Growth Equity</text>
    </svg>
    <figcaption class="page-no">63</figcaption>
  </figure>

  <!-- 64 Agenda: Track Record -->
  <figure class="frame">
    <svg class="slide" viewBox="0 0 194 146">
      <polygon points="116,0 194,0 194,146 66,146 146,70" fill="var(--sky)"/>
      <text class="t-agenda" x="33" y="38">› Executive Summary</text>
      <text class="t-agenda" x="33" y="49">› Differentiated Model</text>
      <text class="t-agenda-on" x="32" y="61">›Track Record</text>
      <text class="t-agenda" x="33" y="72">› Summary of Terms</text>
      <text class="t-agenda" x="33" y="83">› Appendix</text>
      <text x="6" y="142" class="t-logo-lg">Harlow</text>
    </svg>
    <figcaption class="page-no">64</figcaption>
  </figure>

  <!-- 65 Conclusions, numbered -->
  <figure class="frame">
    <svg class="slide" viewBox="0 0 194 146">
      <text x="5" y="12" class="t-title">Conclusions</text>
      <text x="189" y="12" text-anchor="end" class="t-logo">Harlow</text>
      <line x1="5" y1="18" x2="189" y2="18" class="rule"/>
      <rect x="20" y="30" width="144" height="15" fill="var(--sky-soft)"/>
      <rect x="20" y="51" width="144" height="15" fill="var(--cream)"/>
      <rect x="20" y="72" width="144" height="15" fill="var(--teal)"/>
      <rect x="20" y="93" width="144" height="14" fill="var(--mint)"/>
      <g fill="#fff" opacity=".45"><rect x="20" y="30" width="13" height="15"/><rect x="20" y="51" width="13" height="15"/><rect x="20" y="72" width="13" height="15"/><rect x="20" y="93" width="13" height="14"/></g>
      <g class="t-tiny" font-size="3" font-weight="700"><text x="24" y="39">01</text><text x="24" y="60">02</text><text x="24" y="81">03</text><text x="24" y="102">04</text></g>
      <text class="t-tiny" font-size="2.6" x="38" y="38.5">Cohesive team with 20+ years of working together</text>
      <text class="t-tiny" font-size="2.6"><tspan x="38" y="57">Compelling opportunity in lower-middle market buyouts and</tspan><tspan x="38" y="60.5">growth equity in private, recurring revenue software companies</tspan></text>
      <text class="t-tiny" font-size="2.6"><tspan x="38" y="78">Repeatable, proprietary, analytics-driven model for sourcing executives</tspan><tspan x="38" y="81.5">and investment prospects</tspan></text>
      <text class="t-tiny" font-size="2.6" x="38" y="101">Proven, ability to deliver above market, risk-balanced returns of 3-5x</text>
      <line x1="10" y1="131" x2="184" y2="131" class="foot-rule"/>
      <text x="10" y="138" class="t-foot">Confidential 65</text>
      <text x="184" y="138" text-anchor="end" class="t-brand">HL Growth Equity</text>
    </svg>
    <figcaption class="page-no">65</figcaption>
  </figure>

  <!-- 66 Conclusions, bullets -->
  <figure class="frame">
    <svg class="slide" viewBox="0 0 194 146">
      <text x="5" y="12" class="t-title">Conclusions</text>
      <text x="189" y="12" text-anchor="end" class="t-logo">Harlow</text>
      <line x1="5" y1="18" x2="189" y2="18" class="rule"/>
      <g fill="var(--sky)"><circle cx="28" cy="41" r=".9"/><circle cx="28" cy="53" r=".9"/><circle cx="28" cy="72" r=".9"/><circle cx="28" cy="90" r=".9"/></g>
      <text class="t-bul" x="31" y="42">Cohesive team with 20+ years of working together</text>
      <text class="t-bul"><tspan x="31" y="54">Compelling opportunity in lower-middle market buyouts and growth equity</tspan><tspan x="31" y="58.5">in private, recurring revenue software companies</tspan></text>
      <text class="t-bul"><tspan x="31" y="73">Repeatable, proprietary, analytics-driven model for sourcing executives and</tspan><tspan x="31" y="77.5">investment prospects.</tspan></text>
      <text class="t-bul" x="31" y="91">Proven, ability to deliver above market, risk-balanced returns of 3-5x</text>
      <line x1="10" y1="131" x2="184" y2="131" class="foot-rule"/>
      <text x="10" y="138" class="t-foot">Confidential 66</text>
      <text x="184" y="138" text-anchor="end" class="t-brand">HL Growth Equity</text>
    </svg>
    <figcaption class="page-no">66</figcaption>
  </figure>

  <!-- 67 Conclusions, diagonal accent -->
  <figure class="frame">
    <svg class="slide" viewBox="0 0 194 146">
      <polygon points="157,0 179,0 100,146 78,146" fill="var(--teal)"/>
      <polygon points="179,0 194,0 194,141 89,141 100,146 89,146" fill="var(--sky)"/>
      <text x="5" y="12" class="t-title">Conclusions</text>
      <line x1="5" y1="18" x2="150" y2="18" class="rule"/>
      <g fill="var(--sky)"><circle cx="15" cy="34" r=".9"/><circle cx="15" cy="47" r=".9"/><circle cx="15" cy="70" r=".9"/><circle cx="15" cy="88" r=".9"/></g>
      <text class="t-bul" x="19" y="35">Cohesive team with 20+ years of working together</text>
      <text class="t-bul"><tspan x="19" y="48">Compelling opportunity in lower-middle market</tspan><tspan x="19" y="52.5">buyouts and growth equity in private, recurring</tspan><tspan x="19" y="57">revenue software companies</tspan></text>
      <text class="t-bul"><tspan x="19" y="71">Repeatable, proprietary, analytics-driven model</tspan><tspan x="19" y="75.5">for sourcing executives and investment prospects.</tspan></text>
      <text class="t-bul"><tspan x="19" y="89">Proven, ability to deliver above market, risk-</tspan><tspan x="19" y="93.5">balanced returns of 3-5x</tspan></text>
      <line x1="10" y1="131" x2="90" y2="131" class="foot-rule"/>
      <text x="10" y="138" class="t-foot">Confidential 67</text>
    </svg>
    <figcaption class="page-no">67</figcaption>
  </figure>

  <!-- 68 Agenda: Appendix -->
  <figure class="frame">
    <svg class="slide" viewBox="0 0 194 146">
      <polygon points="116,0 194,0 194,146 113,146 146,69" fill="var(--sky)"/>
      <text class="t-agenda" x="31" y="39">› Executive Summary</text>
      <text class="t-agenda" x="31" y="49">› Differentiated Model</text>
      <text class="t-agenda" x="31" y="59">› Track Record</text>
      <text class="t-agenda" x="31" y="70">› Summary of Terms</text>
      <text class="t-agenda-on" x="30" y="82">›Appendix</text>
      <text x="6" y="142" class="t-logo-lg">Harlow</text>
    </svg>
    <figcaption class="page-no">68</figcaption>
  </figure>

  <!-- 69 Important information, dense -->
  <figure class="frame">
    <svg class="slide" viewBox="0 0 194 146">
      <text x="5" y="12" class="t-title">Important Information</text>
      <text x="189" y="12" text-anchor="end" class="t-logo">Harlow</text>
      <line x1="5" y1="18" x2="189" y2="18" class="rule"/>
      <foreignObject x="10" y="21" width="174" height="108">
        <div xmlns="http://www.w3.org/1999/xhtml" class="prose" style="font-size:2px;line-height:2.5px">
          <p>This presentation is provided for information only and does not constitute an offer to sell or a solicitation of an offer to buy any interest in any fund. Any offer will be made only by a confidential offering memorandum and related documents, which should be read in full before investing. Past performance is not indicative of future results and there can be no assurance that targets will be met.</p>
          <p>Certain information contained herein has been obtained from third party sources believed to be reliable, but its accuracy and completeness cannot be guaranteed. Opinions and estimates are subject to change without notice and reflect judgment as of the date shown. Returns shown are gross unless stated otherwise and do not reflect fees, carried interest, taxes or expenses that will reduce actual returns to investors.</p>
          <p>Forward looking statements involve known and unknown risks, uncertainties and other factors which may cause actual results to differ materially from those expressed or implied. Investors should not place undue reliance on such statements. Private equity investments are speculative, illiquid and involve a high degree of risk, including the possible loss of the entire amount invested.</p>
          <p>This document is confidential and may not be reproduced or distributed, in whole or in part, without prior written consent. Recipients should consult their own legal, tax and financial advisers before making any investment decision. Interests have not been registered under any securities laws and may only be offered to qualified investors in permitted jurisdictions.</p>
        </div>
      </foreignObject>
      <line x1="10" y1="131" x2="184" y2="131" class="foot-rule"/>
      <text x="10" y="138" class="t-foot">Confidential 69</text>
      <text x="184" y="138" text-anchor="end" class="t-brand">HL Growth Equity</text>
    </svg>
    <figcaption class="page-no">69</figcaption>
  </figure>

  <!-- 70 Important information, light -->
  <figure class="frame">
    <svg class="slide" viewBox="0 0 194 146">
      <text x="5" y="12" class="t-title">Important Information</text>
      <text x="189" y="12" text-anchor="end" class="t-logo">Harlow</text>
      <line x1="5" y1="18" x2="189" y2="18" class="rule"/>
      <foreignObject x="13" y="32" width="168" height="96">
        <div xmlns="http://www.w3.org/1999/xhtml" class="prose" style="font-size:2.3px;line-height:2.9px">
          <p>This presentation has been prepared solely for use by prospective investors of the fund and should be read with the offering memorandum. It may not be copied or shared without the written consent of the general partner and its manager.</p>
          <p>The presentation is not an offer of securities. Any investment involves risk, including loss of capital, and no assurance can be given that the fund will achieve its objectives or avoid losses.</p>
          <p>Neither the fund nor its manager makes any representation as to the accuracy of figures from third parties. Returns, targets and projections are estimates only and may change without notice.</p>
          <p>The interests have not been registered under the securities act and may not be sold except under an available exemption. Investors should seek independent advice on the legal and tax implications.</p>
        </div>
      </foreignObject>
      <line x1="10" y1="131" x2="184" y2="131" class="foot-rule"/>
      <text x="10" y="138" class="t-foot">Confidential 70</text>
      <text x="184" y="138" text-anchor="end" class="t-brand">HL Growth Equity</text>
    </svg>
    <figcaption class="page-no">70</figcaption>
  </figure>

  <!-- 71 Contact -->
  <figure class="frame">
    <svg class="slide" viewBox="0 0 194 146">
      <polygon points="0,0 87,0 54,72 87,146 0,146" fill="var(--sky)"/>
      <text x="81" y="35" class="t-tiny" font-size="2.4">OFFICE &amp; SOCIAL ADDRESS</text>
      <text x="81" y="45" class="t-contact-h">CONTACT US</text>
      <text x="81" y="51" class="t-tiny" font-size="2.4">GET IN TOUCH</text>
      <text x="81" y="60" class="t-tiny" font-size="2" fill="#f2a900" font-weight="700">ABOUT</text>
      <text class="t-tiny" font-size="2"><tspan x="81" y="64">Growth equity partner to founder led software companies across</tspan><tspan x="81" y="67">North America and Europe since 1998.</tspan></text>
      <g fill="var(--dark)">
        <path d="M81.5 91.2 q.4 -.8 1.1 0 l.5 .6 q.2 .4 -.2 .7 q.6 1 1.4 1.4 q.3 -.4 .7 -.2 l.6 .5 q.7 .6 0 1 q-1 .7 -2.4 -.4 q-1.4 -1.2 -1.7 -2.2 q-.2 -.8 0 -1.4z"/>
        <rect x="81.3" y="98" width="3.6" height="2.6" rx=".3"/>
        <circle cx="83.1" cy="106.4" r="1.7"/>
        <rect x="133" y="91" width="3.2" height="3.2" rx=".4"/>
        <rect x="133" y="98" width="3.2" height="3.2" rx=".4"/>
        <rect x="133" y="105" width="3.2" height="3.2" rx=".4"/>
      </g>
      <polyline points="81.4,98.2 83.1,99.6 84.8,98.2" fill="none" stroke="#fff" stroke-width=".3"/>
      <g class="t-tiny" font-size="2"><text x="88" y="93.5">+1 555 010 2040</text><text x="88" y="100.5">hello@harlowge.com</text><text x="88" y="107.5">www.harlowge.com</text>
        <text x="139" y="93.5">/harlowgrowth</text><text x="139" y="100.5">@harlowgrowth</text><text x="139" y="107.5">in/harlowgrowth</text></g>
    </svg>
    <figcaption class="page-no">71</figcaption>
  </figure>

</main>
</body>
</html>
```